Ternhollow Partners

Need a new website - see more on ternhollowpartners.example

Target Market(s)

Finance industry = conservative design

Coding

Coded - Design and coding required

Number of Pages Required

5+ page

Requirements
Should not have
• Dear all,
• Please avoid pictures of people on the website (except the "team" of course :-)

```html
<!DOCTYPE html>
<html lang="en">
<head>
<meta charset="utf-8">
<title>Ternhollow Partners</title>
<link rel="stylesheet" href="https://fonts.googleapis.com/css2?family=Raleway:wght@400;500;600;700&family=Open+Sans:wght@400;600&family=Tinos&display=swap">
<style>
:root{
  --red:#d3262c;
  --ink:#222;
  --white:#fff;
  --band:#231f20;
  --light:#efefef;
  --navy:#0d1526;
  --field:#fafafa;
  --line:#d8d8d8;
}
*{margin:0;padding:0;box-sizing:border-box}
html,body{width:1200px;height:3030px;overflow:hidden;background:var(--white)}
body{position:relative;font-family:"Open Sans",Arial,sans-serif;color:var(--ink)}
.abs{position:absolute}

/* header */
.topbar{left:687px;top:0;width:513px;height:28px;background:var(--red);color:var(--white);font-size:15px;display:flex;align-items:center;gap:14px;padding-left:52px;clip-path:polygon(18px 0,100% 0,100% 100%,0 100%)}
.topbar .sep{width:1px;height:16px;background:rgba(255,255,255,.6)}
.topbar span{display:flex;align-items:center;gap:6px}
.brand{left:141px;top:30px;height:80px;display:flex;align-items:center;gap:12px}
.brand .dot{width:78px;height:78px;border-radius:50%;background:var(--red)}
.brand .name{font-family:"Raleway",Arial,sans-serif;font-weight:600;font-size:26px;line-height:27px;color:var(--ink);text-transform:uppercase;width:150px}
.nav{left:516px;top:92px;display:flex;gap:32px;font-size:15px;color:var(--ink)}
.nav .active{color:var(--red)}

/* hero */
.hero{left:0;top:130px;width:1200px;height:460px;background:linear-gradient(180deg,#6f9cc8 0%,#a9c3d9 28%,#8a8f86 55%,#56703f 80%,#3f5a2e 100%)}
.hero-curve{left:0;top:500px}
.hero-title{left:0;top:285px;width:1200px;text-align:center;color:var(--white);font-family:"Raleway",Arial,sans-serif;font-weight:600;font-size:40px;line-height:47px;text-shadow:0 2px 4px rgba(0,0,0,.45)}
.btn-dark{background:#2b2b2b;color:var(--white);font-size:15px;padding:6px 14px}
.arrow{width:34px;height:32px;background:#2b2b2b;display:flex;align-items:center;justify-content:center}

/* section titles */
.sec-title{left:0;width:1200px;text-align:center;font-family:"Raleway",Arial,sans-serif;font-size:33px;font-weight:500;color:var(--ink)}
.rule{width:76px;height:3px;background:var(--red);left:562px}

/* services */
.services-intro{left:200px;top:648px;width:800px;text-align:center;font-size:13.5px;line-height:22px;color:#333}
.service-icon{width:90px;height:90px;border-radius:50%;background:var(--red);display:flex;align-items:center;justify-content:center;box-shadow:0 2px 4px rgba(0,0,0,.25)}
.service-label{width:300px;text-align:center;font-size:13.5px;font-weight:600;color:var(--ink)}
.service-box{width:283px;height:65px;background:linear-gradient(180deg,#fff 0%,#e1e1e1 100%);text-align:center;font-size:11px;line-height:17px;color:#333;padding:8px 16px 0}

/* welcome */
.welcome{left:0;top:966px;width:1200px;height:472px;background:linear-gradient(180deg,#3a3a3a 0%,#262626 45%,#1a1a1a 100%)}
.welcome-title{left:0;top:1060px;width:1200px;text-align:center;color:var(--white);font-family:"Raleway",Arial,sans-serif;font-weight:500;font-size:32px}
.welcome-rule{left:562px;top:1108px;width:76px;height:2px;background:var(--white)}
.welcome-text{left:160px;top:1126px;width:880px;text-align:center;color:var(--white);font-size:11.5px;line-height:24px}
.btn-red{background:var(--red);color:var(--white);font-size:15px;padding:7px 16px}

/* engagements */
.engage-card{top:1588px;width:293px;height:202px;border:3px solid var(--red);border-radius:12px}
.engage-url{top:1804px;width:293px;text-align:center;font-size:13.5px;font-weight:600;color:var(--ink)}

/* team */
.lead-photo{left:178px;top:1955px;width:210px;height:210px;border-radius:50%;border:5px solid var(--red);background:radial-gradient(circle at 50% 40%,#c7a188 0%,#9b6a55 45%,#4a3c43 100%)}
.bio-name{left:424px;top:1990px;font-size:17px;color:var(--ink)}
.bio-name small{font-size:12px;color:#777}
.bio{left:424px;top:2016px;width:580px;font-size:11px;line-height:23px;color:#333}
.thumb{width:72px;height:72px;border-radius:50%;border:3px solid #eee;background:radial-gradient(circle at 50% 40%,#cfb2a0 0%,#90776b 55%,#5a5560 100%)}
.thumb-label{width:130px;text-align:center;font-size:10.5px;line-height:14px;color:#333}

/* offices band */
.offices{left:0;top:2300px;width:1200px;height:225px;background:var(--band);color:var(--white);text-align:center}
.offices h2{position:absolute;left:0;top:20px;width:1200px;font-family:"Raleway",Arial,sans-serif;font-weight:500;font-size:32px}
.offices p{position:absolute;left:0;top:70px;width:1200px;font-family:"Raleway",Arial,sans-serif;font-size:20px;line-height:39px;color:var(--white)}
.offices .btn-dark{position:absolute;left:524px;top:172px;background:#3a3a3a}

/* contact */
.contact{left:0;top:2525px;width:1200px;height:400px;background:var(--light)}
.contact-title{left:156px;top:2582px;font-family:"Raleway",Arial,sans-serif;font-size:18px;color:var(--ink);border-bottom:1px solid var(--ink);padding-bottom:1px}
.city{left:156px;font-size:14px;font-weight:600;color:var(--red)}
.addr{left:156px;font-size:12.5px;line-height:18px;color:#333}
.phone{left:450px;display:flex;align-items:center;gap:8px;font-family:"Tinos",serif;font-size:17px;color:var(--red)}
.field{left:687px;width:355px;height:32px;background:var(--field);border:1px solid var(--line);font-size:11.5px;color:#777;padding:8px 9px}
.submit{left:687px;top:2797px;width:103px;height:33px;background:#111;color:var(--white);font-size:13px;font-weight:600;display:flex;align-items:center;justify-content:center;letter-spacing:.5px}

/* footer */
.footer-wave{left:0;top:2840px}
.foot-brand{left:141px;top:2908px;display:flex;align-items:center;gap:10px}
.foot-brand .dot{width:68px;height:68px;border-radius:50%;background:#9b9ea4}
.foot-brand .name{font-family:"Raleway",Arial,sans-serif;font-weight:600;font-size:21px;line-height:22px;color:#c6c8cc;text-transform:uppercase;width:130px}
.foot-nav{left:156px;top:2994px;display:flex;gap:14px;font-size:12px;color:var(--white)}
.foot-nav .active{color:var(--red)}
.follow{left:860px;top:2962px;font-size:12px;color:var(--white)}
.social{left:940px;top:2956px;display:flex;gap:6px}
.social span{width:26px;height:26px;border-radius:50%;border:2px solid var(--white)}
.copyright{left:740px;top:2994px;font-size:12px;color:var(--white)}
</style>
</head>
<body>

<div class="abs topbar">
  <span><svg width="16" height="16" viewBox="0 0 16 16"><circle cx="8" cy="8" r="7" fill="none" stroke="#fff" stroke-width="1.4"/><path d="M5 4.5c.6-.4 1.2 0 1.4.6l.3.9c.1.4 0 .7-.3.9l-.4.3c.5 1 1.2 1.7 2.2 2.2l.3-.4c.2-.3.5-.4.9-.3l.9.3c.6.2 1 .8.6 1.4-.6.9-1.7 1.1-2.7.6C6.5 10 5.5 9 4.8 7.3c-.5-1-.3-2.1.2-2.8z" fill="#fff"/></svg>555.014.2290</span>
  <span class="sep"></span>
  <span><svg width="16" height="12" viewBox="0 0 16 12"><rect x="1" y="1" width="14" height="10" fill="none" stroke="#fff" stroke-width="1.4"/><path d="M1 1l7 6 7-6" fill="none" stroke="#fff" stroke-width="1.4"/></svg>ternhollowpartners.example</span>
</div>

<div class="abs brand">
  <span class="dot"></span>
  <span class="name">Ternhollow Partners</span>
</div>

<nav class="abs nav">
  <span class="active">Home</span><span>Services</span><span>Current Engagements</span><span>News</span><span>Team</span><span>Contact Us</span>
</nav>

<div class="abs hero" role="img" aria-label="Photograph of a European city skyline with modern office towers, rooftops and trees"></div>
<svg class="abs hero-curve" width="1200" height="95" viewBox="0 0 1200 95"><path d="M0 50 Q600 -40 1200 55 L1200 95 L0 95 Z" fill="#fff"/></svg>
<h1 class="abs hero-title">We Are A Privately Held Global Investment<br>Holding Group</h1>
<div class="abs btn-dark" style="left:527px;top:395px">Contact Us Today</div>
<div class="abs arrow" style="left:0;top:340px"><svg width="10" height="14" viewBox="0 0 10 14"><path d="M8 1L2 7l6 6" fill="none" stroke="#fff" stroke-width="2.4"/></svg></div>
<div class="abs arrow" style="left:1166px;top:340px"><svg width="10" height="14" viewBox="0 0 10 14"><path d="M2 1l6 6-6 6" fill="none" stroke="#fff" stroke-width="2.4"/></svg></div>

<h2 class="abs sec-title" style="top:588px">Our Services</h2>
<div class="abs rule" style="top:636px"></div>
<p class="abs services-intro">Lorem ipsum dolor sit amet, conseLoLorem ipsum dolor sit amet, consectetuer adipiscing elitrem ipsum dolor sit amet, consectetuer adipiscing elitctetuer adipiscing elit</p>

<div class="abs service-icon" style="left:244px;top:713px"><svg width="46" height="30" viewBox="0 0 46 30"><path d="M2 10l10-6 8 3 6-3 18 8-6 6" fill="none" stroke="#fff" stroke-width="3" stroke-linejoin="round"/><path d="M12 16l8 8c1 1 3 1 4 0l8-8" fill="none" stroke="#fff" stroke-width="3" stroke-linecap="round"/></svg></div>
<div class="abs service-icon" style="left:553px;top:713px"><svg width="30" height="44" viewBox="0 0 30 44"><path d="M15 4v36M15 4l-7 8M15 4l7 8" fill="none" stroke="#fff" stroke-width="3.4" stroke-linecap="round"/><circle cx="15" cy="24" r="6" fill="#fff"/></svg></div>
<div class="abs service-icon" style="left:864px;top:713px"><svg width="42" height="42" viewBox="0 0 42 42"><rect x="4" y="4" width="15" height="15" fill="#fff"/><rect x="23" y="4" width="15" height="15" fill="#fff"/><rect x="4" y="23" width="15" height="15" fill="#fff"/><rect x="23" y="23" width="15" height="15" fill="#fff"/></svg></div>

<div class="abs service-label" style="left:139px;top:820px">Private Placements</div>
<div class="abs service-label" style="left:448px;top:816px">Reverse Mergers &amp; Alternative Offerings</div>
<div class="abs service-label" style="left:759px;top:816px">Mergers &amp; Acquisitions</div>

<div class="abs service-box" style="left:147px;top:845px">Lorem ipsum dolor sit amet, consectetuer<br>adipiscing elit, sed diam nonumm</div>
<div class="abs service-box" style="left:457px;top:845px">Lorem ipsum dolor sit amet, consectetuer<br>adipiscing elit, sed diam nonumm</div>
<div class="abs service-box" style="left:767px;top:845px">Lorem ipsum dolor sit amet, consectetuer<br>adipiscing elit, sed diam nonumm</div>

<div class="abs welcome" role="img" aria-label="Dark photograph of an office desk with a laptop and notebook in front of a window overlooking city towers"></div>
<h2 class="abs welcome-title">Welcome To Ternhollow Partners</h2>
<div class="abs welcome-rule"></div>
<p class="abs welcome-text">Lorem ipsum dolor sit amet, consectetuer adipiscing elit, sed diam nonummy nibh euismod tincidunt ut laoreet dolore magna aliquam erat volutpat. Ut wisi enim ad minim veniam, quis nostrud exerci tation ullamcorper suscipid tincidunt ut laoreet dolore magna aliquam erat volutpat. Ut wisi enim ad minim veniam, quis nostrud exerci tation ullamcorper suscipit lobortis nisl ut aliquip ex ea commodo consequat. Duis autem vel eum iriure dolor in hendrerit in vulputate velit esse molestie consequat, vel illum dolore eu feugiat nulla facilisis at vero eros et accumsan et iusto odio dignissim qui blandit praesent luptatum zzril delenit augue duis dolore te feugait nulla facilisi. Duis autem vel eum iriure dolor in hendrerit in vulputate velit esse molestie consequat, vel illum dolore eu feugiat nulla fa loborhs nisl ut aliquip ex ea commodo consequat.</p>
<div class="abs btn-red" style="left:487px;top:1293px">View Ternhollow Services</div>

<h2 class="abs sec-title" style="top:1492px">Current Engagements</h2>
<div class="abs engage-card" style="left:141px;background:linear-gradient(135deg,#2a2a2e 0%,#121214 60%,#3a2f28 100%)" role="img" aria-label="Website screenshot of Lanternpeak, a blockchain venture"></div>
<div class="abs engage-card" style="left:454px;background:linear-gradient(135deg,#5b3a3a 0%,#2a2226 55%,#6d5a55 100%)" role="img" aria-label="Website screenshot of Brightfield Marketing"></div>
<div class="abs engage-card" style="left:767px;background:linear-gradient(135deg,#4b4f57 0%,#2b2d33 55%,#7a6a62 100%)" role="img" aria-label="Website screenshot of Norvale fashion store"></div>
<div class="abs engage-url" style="left:141px">www.lanternpeakledger.example</div>
<div class="abs engage-url" style="left:454px">www.brightfieldmarketing.example</div>
<div class="abs engage-url" style="left:767px">www.norvale.example</div>

<h2 class="abs sec-title" style="top:1880px">Our Team</h2>
<div class="abs rule" style="top:1928px"></div>
<div class="abs lead-photo" role="img" aria-label="Portrait photograph of Anders Holm, Managing Director"></div>
<div class="abs bio-name">Anders Holm, <small>Managing Director</small></div>
<p class="abs bio">Mr. Holm, an international financier, has over 25 years experience in the global financial services industry as a securities professional. From 1996 through 2003, Mr. Holm was Co-Founder and Managing Partner of Quillmere Vantrow Capital in London, in charge of the private placement division of the company. From 1991 through 1996, Mr. Holm was Senior Portfolio Manager of Varrowby Fund Managers, a London-based hedge fund. Mr. Holm started his career in 1986 with Solvikstrand Bank in Copenhagen, Denmark.</p>
<div class="abs thumb" style="left:368px;top:2140px" role="img" aria-label="Small portrait of Anders Holm"></div>
<div class="abs thumb" style="left:479px;top:2140px;background:radial-gradient(circle at 50% 40%,#d0ab93 0%,#8a6a5c 50%,#2f3d66 100%)" role="img" aria-label="Small portrait of Mikkel Brandt"></div>
<div class="abs thumb-label" style="left:339px;top:2224px">Anders Holm,<br>Managing Director</div>
<div class="abs thumb-label" style="left:450px;top:2224px">Mikkel Brandt,<br>Managing Partner</div>

<section class="abs offices">
  <h2>Ternhollow Partners Offices</h2>
  <p>Founded in 2004, Ternhollow is headquartered in Gibraltar with representative offices<br>in Luxembourg and London.</p>
  <div class="btn-dark">Contact Us Today</div>
</section>

<div class="abs contact"></div>
<div class="abs contact-title">Ternhollow Representative Offices</div>

<div class="abs city" style="top:2624px">Beverly Hills</div>
<div class="abs addr" style="top:2646px">210 Linden Court - Suite 400<br>Beverly Hills, CA 90299, United States</div>
<div class="abs city" style="top:2696px">Luxembourg</div>
<div class="abs addr" style="top:2718px">14, Rue des Tilleuls<br>2099 Luxembourg, Luxembourg</div>
<div class="abs city" style="top:2768px">London</div>
<div class="abs addr" style="top:2790px">22 Alder Row<br>SE1 9ZZ London, United Kingdom</div>

<div class="abs phone" style="top:2655px"><svg width="16" height="16" viewBox="0 0 16 16"><circle cx="8" cy="8" r="7" fill="none" stroke="#333" stroke-width="1.3"/><path d="M5 4.5c.6-.4 1.2 0 1.4.6l.3.9c.1.4 0 .7-.3.9l-.4.3c.5 1 1.2 1.7 2.2 2.2l.3-.4c.2-.3.5-.4.9-.3l.9.3c.6.2 1 .8.6 1.4-.6.9-1.7 1.1-2.7.6C6.5 10 5.5 9 4.8 7.3c-.5-1-.3-2.1.2-2.8z" fill="#333"/></svg>+1 310 555 0142</div>
<div class="abs phone" style="top:2730px"><svg width="16" height="16" viewBox="0 0 16 16"><circle cx="8" cy="8" r="7" fill="none" stroke="#333" stroke-width="1.3"/><path d="M5 4.5c.6-.4 1.2 0 1.4.6l.3.9c.1.4 0 .7-.3.9l-.4.3c.5 1 1.2 1.7 2.2 2.2l.3-.4c.2-.3.5-.4.9-.3l.9.3c.6.2 1 .8.6 1.4-.6.9-1.7 1.1-2.7.6C6.5 10 5.5 9 4.8 7.3c-.5-1-.3-2.1.2-2.8z" fill="#333"/></svg>+352 555 010 203</div>
<div class="abs phone" style="top:2803px"><svg width="16" height="16" viewBox="0 0 16 16"><circle cx="8" cy="8" r="7" fill="none" stroke="#333" stroke-width="1.3"/><path d="M5 4.5c.6-.4 1.2 0 1.4.6l.3.9c.1.4 0 .7-.3.9l-.4.3c.5 1 1.2 1.7 2.2 2.2l.3-.4c.2-.3.5-.4.9-.3l.9.3c.6.2 1 .8.6 1.4-.6.9-1.7 1.1-2.7.6C6.5 10 5.5 9 4.8 7.3c-.5-1-.3-2.1.2-2.8z" fill="#333"/></svg>+44 7700 900 226</div>

<div class="abs field" style="top:2584px">Name</div>
<div class="abs field" style="top:2628px">Email</div>
<div class="abs field" style="top:2672px">Phone</div>
<div class="abs field" style="top:2716px;height:68px">Message</div>
<div class="abs submit">SUBMIT</div>

<svg class="abs footer-wave" width="1200" height="190" viewBox="0 0 1200 190">
  <path d="M0 60 Q600 0 1200 40 L1200 190 L0 190 Z" fill="#0d1526"/>
  <path d="M0 54 Q600 -8 1200 30 L1200 40 Q600 4 0 66 Z" fill="#d3262c"/>
  <path d="M0 66 Q600 6 1200 42 L1200 48 Q600 16 0 74 Z" fill="#fff"/>
  <circle cx="933" cy="55" r="34" fill="#d3262c"/>
</svg>
<div class="abs foot-brand"><span class="dot"></span><span class="name">Ternhollow Partners</span></div>
<nav class="abs foot-nav"><span class="active">Home</span><span>Services</span><span>Current Engagements</span><span>News</span><span>Team</span><span>Contact Us</span></nav>
<div class="abs follow">Follow Us</div>
<div class="abs social"><span></span><span></span><span></span><span></span></div>
<div class="abs copyright">Copyright ©2018 TernhollowPartners. All Rights Reserved.</div>

</body>
</html>
```